A label for a bottle of Gin that reflect the area in which it is made - Fernstill

I have attached a couple of labels that we are not very happy with. We are looking for something that portrays a premium brand. The bottle is called Palomere 700ml. and the image should be max 9cm by 7cm. For details on webpage - see notes at fernstill.co.uk/coast and fernstill.co.uk/coastgin. The website should just be a single homepage with a link to fernstill.co.uk/coastgin

The words "Small Batch Handmade Gin" could feature

Number of Pages Required

1 page

Requirements
Nice to have
• Gold or Silver that can add to overall quality feel of the label.
Should not have
• Transparent labels look great when back lit but tend to disappear when on a dark bar with other brighter bottles. Avoid transparency

```html
<!DOCTYPE html>
<html lang="en">
<head>
<meta charset="utf-8">
<title>Fernstill Gin – Label Variants</title>
<link href="https://fonts.googleapis.com/css2?family=EB+Garamond:wght@600;700;800&display=swap" rel="stylesheet">
<style>
  :root {
    --backdrop: #a8a8a8;
    --label-paper: #e4e4e6;
    --ink-black: #111111;
    --ink-red: #a3141f;
    --ink-red-dark: #6a0b13;
    --silver-light: #d4d6da;
    --silver-mid: #8a8d93;
    --silver-dark: #45484e;
    --rule: #1a1a1a;
  }
  * { margin: 0; padding: 0; box-sizing: border-box; }
  html, body {
    width: 1200px; height: 965px; overflow: hidden;
    background: var(--backdrop);
  }
  .stage {
    position: relative; width: 1200px; height: 965px;
    display: flex; align-items: center; justify-content: center; gap: 64px;
  }

  .label {
    position: relative;
    width: 320px; height: 414px;
    background: var(--label-paper);
    font-family: "EB Garamond", Georgia, serif;
    color: var(--ink-black);
    text-align: center;
    flex: none;
  }

  .label__frame {
    position: absolute; inset: 10px;
    border: 1.5px solid var(--ink-red);
  }

  .label__region {
    position: absolute; top: 29px; left: 0; right: 0;
    font-size: 16px; line-height: 16px; font-weight: 700; letter-spacing: 4px;
    padding-left: 4px;
  }
  .label__gin {
    position: absolute; top: 48px; left: 0; right: 0;
    font-size: 80px; line-height: 80px; font-weight: 700; letter-spacing: 1px;
  }
  .label--silver .label__gin {
    background: linear-gradient(100deg, var(--silver-dark) 0%, var(--silver-mid) 22%, var(--silver-light) 42%, var(--silver-mid) 60%, var(--silver-dark) 85%);
    -webkit-background-clip: text; background-clip: text; color: transparent;
  }
  .label--red .label__gin {
    background: linear-gradient(100deg, var(--ink-red-dark) 0%, var(--ink-red) 45%, var(--ink-red-dark) 100%);
    -webkit-background-clip: text; background-clip: text; color: transparent;
  }

  .label__mark {
    position: absolute; top: 192px; left: 0; right: 0;
    display: flex; align-items: center; justify-content: center; gap: 10px;
    font-size: 18px; line-height: 22px; font-weight: 700; letter-spacing: 3px;
  }
  .label__mark-dot {
    width: 14px; height: 14px; border-radius: 50%;
    background: currentColor;
  }
  .label--silver .label__mark { color: var(--silver-mid); }
  .label--red .label__mark { color: var(--ink-red); }

  .label__rule {
    position: absolute; height: 2px; background: var(--rule);
  }
  .label__rule--upper { top: 355px; left: 0; width: 234px; }
  .label__rule--lower { top: 400px; left: 80px; right: 0; }
  .label--red .label__rule--upper { left: 80px; width: 141px; top: 350px; }
  .label--red .label__rule--lower { left: 80px; right: 11px; top: 392px; }

  .label__tagline {
    position: absolute; top: 361px; left: 0; right: 0;
    font-size: 13px; font-weight: 700; letter-spacing: 2px; line-height: 16px;
    padding-left: 2px;
  }
  .label--red .label__tagline { top: 355px; }
</style>
</head>
<body>
<main class="stage">

  <section class="label label--black">
    <p class="label__region">FERNSTILL</p>
    <h1 class="label__gin">GIN</h1>
    <div class="label__mark"><span class="label__mark-dot"></span>FERNSTILL</div>
    <div class="label__rule label__rule--upper"></div>
    <p class="label__tagline">SMALL BATCH<br>HANDMADE GIN</p>
    <div class="label__rule label__rule--lower"></div>
  </section>

  <section class="label label--silver">
    <p class="label__region">FERNSTILL</p>
    <h1 class="label__gin">GIN</h1>
    <div class="label__mark"><span class="label__mark-dot"></span>FERNSTILL</div>
    <div class="label__rule label__rule--upper"></div>
    <p class="label__tagline">SMALL BATCH<br>HANDMADE GIN</p>
    <div class="label__rule label__rule--lower"></div>
  </section>

  <section class="label label--red">
    <div class="label__frame"></div>
    <p class="label__region">FERNSTILL</p>
    <h1 class="label__gin">GIN</h1>
    <div class="label__mark"><span class="label__mark-dot"></span>FERNSTILL</div>
    <div class="label__rule label__rule--upper"></div>
    <p class="label__tagline">SMALL BATCH<br>HANDMADE GIN</p>
    <div class="label__rule label__rule--lower"></div>
  </section>

</main>
</body>
</html>
```